Web Design For Metal Recycling Company

We are a scrap and recycling company dealing mainly in scrap metal base in Singapore. We deal in both domestic market and international market. Currently we are still unsure if we want to have a "lively" or "professional" company image so we will leave it to the designer to deem what is good.

We wish for a website to be able to "Retain" the interest of new visitor and at the same time able to give enough information for new and existing customer. We would also wish for design that will get the visitor to "Engage" us.

The attached is the logo for the company and we would want to incorporate that into the website. Either of the logo is fine.

```html
<!DOCTYPE html>
<html lang="en">
<head>
<meta charset="utf-8">
<title>Kovan Metal – Scrap Metal Recycling</title>
<link href="https://fonts.googleapis.com/css2?family=Ubuntu:ital,wght@0,400;0,500;1,400&display=swap" rel="stylesheet">
<style>
:root{
  --gold:#c9952b;
  --gold-text:#b8932a;
  --navy:#3b3a7a;
  --ink:#333;
  --muted:#666;
  --band:#f4f2e9;
  --grey:#efefef;
  --dark:#262626;
}
*{box-sizing:border-box;margin:0;padding:0}
html,body{width:897px;height:1200px;overflow:hidden;background:#fff}
body{font-family:"Ubuntu",sans-serif;color:var(--ink);font-size:10px}
.page{position:relative;width:897px;height:1200px}
.abs{position:absolute}
a{color:inherit;text-decoration:none}

.brand{left:120px;top:24px;display:flex;align-items:center;gap:8px}
.brand-mark{width:26px;height:26px;border:2px solid var(--gold)}
.brand-name{color:var(--gold);font-size:18px;font-weight:500;letter-spacing:.5px}

.nav-item{top:51px;font-size:12px;color:#555;white-space:nowrap}
.nav-item.active{color:var(--navy)}
.nav-item.active::after{content:"";position:absolute;left:-4px;right:-6px;top:30px;height:2px;background:var(--gold)}
.caret{font-size:8px;margin-left:3px}
.search{left:680px;top:47px;width:101px;height:22px;border:1px solid var(--navy);display:flex}
.search span{flex:1;font-size:9px;color:#999;padding:5px 6px}
.search b{width:24px;background:var(--navy);display:flex;align-items:center;justify-content:center}

.hero{left:0;top:81px;width:897px;height:258px;background:linear-gradient(160deg,#5a5a5e 0%,#3a3a3f 45%,#6b6466 70%,#2e2d31 100%)}
.hero-title{left:115px;top:150px;background:rgba(30,30,30,.75);color:#e9b93a;font-size:27px;padding:2px 8px;font-weight:500}
.hero-sub{left:115px;top:198px;color:#111;font-size:16px}
.hero-text{left:115px;top:227px;width:300px;color:#fff;font-size:10px;line-height:13px}
.more{left:273px;top:266px;width:59px;height:21px;background:var(--gold);color:#fff;font-size:9.5px;display:flex;align-items:center;justify-content:center;border-radius:2px}
.arrow{top:196px;width:32px;height:30px;background:var(--gold);display:flex;align-items:center;justify-content:center}

.dropdown{left:468px;top:83px;width:131px;height:113px;background:var(--gold);padding:2px 7px}
.dropdown div{color:#fff;font-size:11.5px;padding:6px 0 7px;border-bottom:1px solid #f3d999}
.dropdown div:last-child{border:none}

.tabs{left:0;top:339px;width:897px;height:30px;background:var(--band)}
.tab{top:0;height:30px;display:flex;align-items:center;justify-content:center;gap:8px;font-size:11px;color:#444;border-right:1px solid #ddd}
.tab.active{background:var(--navy);color:#fff}

.feature{top:392px;width:165px}
.feature h3{font-size:12.5px;font-weight:400;color:#222;display:flex;align-items:center;gap:5px;margin-bottom:8px}
.feature p{font-size:9.5px;line-height:13.5px;color:#777}

.grey{left:0;top:477px;width:897px;height:236px;background:var(--grey)}
.about{left:115px;top:500px;width:160px}
.about h2{color:var(--gold-text);font-size:13.5px;font-weight:400;margin-bottom:8px}
.about p{font-style:italic;font-size:9px;line-height:12.5px;color:#555;margin-bottom:12px}
.about a{color:var(--navy);font-size:9.5px}

.popup{left:285px;top:437px;width:194px;height:254px;background:#fff;border:1px solid #ddd;padding:12px 9px}
.popup h4{font-size:13px;font-weight:400;color:#222;margin-bottom:7px}
.popup p{font-size:9px;line-height:14px;color:var(--gold-text);margin-bottom:10px}

.card{top:500px;width:131px;height:191px;background:var(--navy);text-align:center;color:#fff;padding-top:22px}
.card h3{color:var(--gold);font-size:16.5px;font-weight:400;letter-spacing:1px;margin:6px 0 6px}
.card p{font-size:9.5px;line-height:14px;padding:0 9px}

.service{top:775px;width:165px}
.service .icon{height:50px;padding-left:22px}
.service h3{color:var(--gold-text);font-size:14px;font-weight:400;margin:24px 0 4px}
.service p{font-size:9.5px;line-height:13.5px;color:#666}

.footer{left:0;top:951px;width:897px;height:104px;background:var(--navy);color:#fff}
.flinks{left:93px;top:18px;font-size:9.5px}
.flinks span{margin:0 3px}
.fhead{font-style:italic;font-size:14px;color:#b6b4df}
.subscribe{left:410px;top:993px;width:166px;height:20px;background:#eee;display:flex}
.subscribe span{flex:1;font-style:italic;font-size:9.5px;color:#888;padding:4px 7px}
.subscribe b{width:28px;background:#e4dfc6;display:flex;align-items:center;justify-content:center}
.social{top:1021px;width:20px;height:20px;border:1.5px solid #fff;border-radius:50%}
.address{left:679px;top:989px;width:140px;font-size:9px;line-height:12px;color:#b6b4df}

.map{left:0;top:1055px;width:897px;height:122px;background:linear-gradient(90deg,#a9c8e0 0%,#e9e4d6 30%,#efe9da 65%,#b9d2e3 100%)}
.closemap{left:415px;top:1098px;width:70px;height:18px;background:#fff;border:1px solid #ccc;font-size:9.5px;color:var(--gold-text);display:flex;align-items:center;justify-content:center;gap:4px}
.copy{left:0;top:1177px;width:897px;height:23px;background:var(--dark);color:#fff;font-size:9.5px;padding:6px 115px}
</style>
</head>
<body>
<div class="page">

  <header>
    <div class="abs brand"><span class="brand-mark"></span><span class="brand-name">KOVAN METAL</span></div>
    <nav>
      <span class="abs nav-item" style="left:416px">Home<span class="caret">⌄</span></span>
      <span class="abs nav-item active" style="left:471px">Products<span class="caret">⌄</span></span>
      <span class="abs nav-item" style="left:540px">Services<span class="caret">⌄</span></span>
      <span class="abs nav-item" style="left:604px">Locations<span class="caret">⌄</span></span>
    </nav>
    <div class="abs search"><span>Search</span><b><svg width="11" height="11" viewBox="0 0 12 12"><circle cx="5" cy="5" r="3.6" fill="none" stroke="#fff" stroke-width="1.8"/><line x1="7.6" y1="7.6" x2="11" y2="11" stroke="#fff" stroke-width="2"/></svg></b></div>
  </header>

  <section>
    <div class="abs hero" role="img" aria-label="Photograph of stacked steel billets"></div>
    <div class="abs hero-title">Lorem ipsum</div>
    <div class="abs hero-sub">Temporibus autem quibusdam</div>
    <div class="abs hero-text">Itaque earum rerum hic tenetur a sapiente delectus, ut aut reiciendis voluptatibus.</div>
    <div class="abs more">More ▸</div>
    <div class="abs arrow" style="left:0"><svg width="16" height="14" viewBox="0 0 16 14"><path d="M8 1 2 7l6 6M2 7h13" fill="none" stroke="#fff" stroke-width="2.5"/></svg></div>
    <div class="abs arrow" style="left:864px"><svg width="16" height="14" viewBox="0 0 16 14"><path d="M8 1l6 6-6 6M14 7H1" fill="none" stroke="#fff" stroke-width="2.5"/></svg></div>
    <div class="abs dropdown">
      <div>Ferrous Scrap</div><div>Non-Ferrous Scrap</div><div>Secondary Steel Scrap</div><div>Rerollable Steel Scrap</div>
    </div>
  </section>

  <div class="abs tabs">
    <div class="abs tab active" style="left:193px;width:118px"><svg width="11" height="11" viewBox="0 0 12 12"><circle cx="6" cy="6" r="4" fill="none" stroke="#c9952b" stroke-width="3" stroke-dasharray="2 1.2"/></svg>Ferrous Scrap</div>
    <div class="abs tab" style="left:311px;width:144px"><svg width="8" height="12"><rect x="2" y="1" width="4" height="10" fill="#c9952b"/></svg>Non-Ferrous Scrap</div>
    <div class="abs tab" style="left:455px;width:145px"><svg width="12" height="12"><circle cx="6" cy="6" r="5" fill="none" stroke="#c9952b" stroke-width="1.3"/><path d="M5 3.5 8 6 5 8.5z" fill="#c9952b"/></svg>Recycling Process</div>
    <div class="abs tab" style="left:600px;width:111px"><svg width="13" height="10"><rect width="13" height="10" fill="#c9952b"/><path d="M0 0l6.5 5L13 0" fill="none" stroke="#fff"/></svg>Contact us</div>
  </div>

  <section>
    <div class="abs feature" style="left:114px"><h3><svg width="20" height="24"><rect x="3" y="3" width="14" height="20" rx="2" fill="#c9952b"/></svg>FERROUS SCRAP</h3><p>Nemo enim ipsam voluptatem quia voluptas sit aspernatur aut odit aut fugit, sed quia consequuntur.</p></div>
    <div class="abs feature" style="left:284px"><h3><svg width="20" height="24"><rect x="7" y="2" width="6" height="4" fill="#c9952b"/><rect x="2" y="6" width="16" height="17" rx="5" fill="#c9952b"/></svg>NON-FERROUS SCRAP</h3><p>Itaque earum rerum hic tenetur a sapiente delectus, ut aut reiciendis.</p></div>
    <div class="abs feature" style="left:455px"><h3><svg width="24" height="24"><rect x="2" y="3" width="15" height="18" rx="2" fill="#c9952b"/><rect x="5" y="6" width="9" height="6" fill="#fff"/><rect x="19" y="3" width="3" height="10" fill="#c9952b"/></svg>USED MACHINERY</h3><p>Duis aute irure dolor in reprehenrit in voluptate velit esse cillum dolore fugiat nulla pariatur.</p></div>
    <div class="abs feature" style="left:625px"><h3><svg width="24" height="24"><path d="M3 22h10M7 22V10l10-5" fill="none" stroke="#c9952b" stroke-width="3"/><circle cx="19" cy="5" r="3" fill="#c9952b"/></svg>REROLLABLE SCRAP</h3><p>Perspiciatis unde omnis iste natus error sit voluptatem accusantium doloremque laudantium.</p></div>
  </section>

  <section>
    <div class="abs grey"></div>
    <div class="abs about">
      <h2>About Us</h2>
      <p>Nemo enim ipsam voluptatem quia voluptas sit aspernatur aut odit aut fugit, sed quia .</p>
      <p>Ut enim ad minima veniam, quis nostrum exercitationem ullam corporis suscipit laboriosam.</p>
      <p>Quis autem vel eum iure reprehenderit qui in ea voluptate velit esse quam.</p>
      <a>Read More ›</a>
    </div>
    <div class="abs popup">
      <h4>Lorem Ipsum</h4><p>Nam libero tempore, cum soluta nobis est eligendi optio cumque nihil impedit quo minus id quod maxime placeat.</p>
      <h4>Temporibus Autem</h4><p>voluptates repudiandae sint et molestiae non recusandae. Itaque earum rerum hic tenetur a sapiente delectus.</p>
      <h4>Neque porro quisquam</h4><p>Ut enim ad minima veniam, quis nostrum exercitationem ullam corporis suscipit laboriosam.</p>
    </div>
    <div class="abs card" style="left:500px">
      <svg width="40" height="38" viewBox="0 0 40 38"><g fill="#fff"><path d="M2 2l8 0-3 3 6 6-2 2-6-6-3 3z"/><path d="M38 2l-8 0 3 3-6 6 2 2 6-6 3 3z"/><path d="M2 36l8 0-3-3 6-6-2-2-6 6-3-3z"/><path d="M38 36l-8 0 3-3-6-6 2-2 6 6 3-3z"/></g></svg>
      <h3>REDUCE</h3><p>Temporibus autem quibusdam et aut officiis debitis aut rerum necessitatibus saepe eveniet ut et voluptates .</p>
    </div>
    <div class="abs card" style="left:649px">
      <svg width="40" height="38" viewBox="0 0 40 38"><g fill="none" stroke="#ddd" stroke-width="5"><path d="M14 8 20 2l6 10"/><path d="M33 18l4 9H24"/><path d="M15 33H5l5-10"/></g></svg>
      <h3>RECYCLE</h3><p>Temporibus autem quibusdam et aut officiis debitis aut rerum necessitatibus saepe eveniet ut et voluptates .</p>
    </div>
  </section>

  <section>
    <div class="abs service" style="left:114px"><div class="icon"><svg width="70" height="46" viewBox="0 0 70 46"><g fill="none" stroke="#444" stroke-width="2.5" stroke-linejoin="round" stroke-linecap="round"><path d="M2 10l10-4 8 20-10 4z" fill="#444"/><path d="M68 10l-10-4-8 20 10 4z" fill="#444"/><path d="M16 12l10-3h10l6 3"/><path d="M54 12l-8-1-12 8a3 3 0 0 0 4 4l8-4"/><path d="M18 24l6 6M23 21l8 8M28 19l9 9M33 18l10 10"/><path d="M18 24l14 12a3 3 0 0 0 4-1l12-9"/></g></svg></div><h3>Our Business</h3><p>Lorem ipsum dolor sit amet, consectetur adipisicing elit, sed do eiusmod tempor incididunt.</p></div>
    <div class="abs service" style="left:284px"><div class="icon"><svg width="58" height="44"><path d="M2 24h54l-6 14H8z" fill="none" stroke="#444" stroke-width="2.5"/><rect x="14" y="14" width="16" height="10" fill="none" stroke="#444" stroke-width="2.5"/><line x1="19" y1="4" x2="19" y2="14" stroke="#444" stroke-width="2.5"/><path d="M2 42q7-4 14 0t14 0 14 0 12 0" fill="none" stroke="#444" stroke-width="2"/></svg></div><h3>Cargo Stuffing</h3><p>Duis aute irure dolor in reprehenderit in voluptate velit esse cillum dolore eu fugiat.</p></div>
    <div class="abs service" style="left:455px"><div class="icon"><svg width="44" height="44"><circle cx="22" cy="22" r="16" fill="none" stroke="#555" stroke-width="8" stroke-dasharray="5 3"/><circle cx="22" cy="22" r="8" fill="none" stroke="#555" stroke-width="3"/></svg></div><h3>Breaking and Cutting</h3><p>Excepteur sint occaecat cupidatat non proident, sunt in culpa qui officia deserunt mollit anim.</p></div>
    <div class="abs service" style="left:625px"><div class="icon"><svg width="52" height="44"><rect x="18" y="4" width="32" height="28" rx="2" fill="none" stroke="#555" stroke-width="2.5"/><path d="M18 14H8L3 22v12h15" fill="none" stroke="#555" stroke-width="2.5"/><circle cx="12" cy="36" r="5" fill="#fff" stroke="#555" stroke-width="2.5"/><circle cx="38" cy="36" r="5" fill="#fff" stroke="#555" stroke-width="2.5"/></svg></div><h3>Transport services</h3><p>Quis autem vel eum iure reprehenderit qui in ea voluptate velit esse.</p></div>
  </section>

  <footer>
    <div class="abs footer">
      <div class="abs flinks">Home<span>|</span>About Us<span>|</span> Careers<span>|</span>Contact Us<span>|</span>Services</div>
      <div class="abs fhead" style="left:410px;top:16px">Subscribe</div>
      <div class="abs fhead" style="left:679px;top:16px">Address</div>
    </div>
    <div class="abs subscribe"><span>Enter your E-mail</span><b><svg width="11" height="8"><rect width="11" height="8" fill="#c9952b"/><path d="M0 0l5.5 4L11 0" fill="none" stroke="#fff"/></svg></b></div>
    <div class="abs social" style="left:450px"></div>
    <div class="abs social" style="left:475px"></div>
    <div class="abs social" style="left:500px"></div>
    <div class="abs social" style="left:525px"></div>
    <div class="abs address">114 ,Sunt in culpa qui officia deserunt mollitia anim.</div>

    <div class="abs map" role="img" aria-label="Street map showing the company location"></div>
    <div class="abs closemap"><svg width="8" height="11"><path d="M4 11 0.5 5A3.5 3.5 0 1 1 7.5 5z" fill="#c9952b"/></svg>Close Map</div>
    <div class="abs copy">copyright © 2014</div>
  </footer>

</div>
</body>
</html>
```